Recipe Card Design

I have a small kitchen store in Livingston Montana, and I would like to have recipe cards (4x6 postcard) designed with my logo, lines for recipe writing, all in black and white. My website is here: www.brambleforkpantry.com

Store

```html
<!DOCTYPE html>
<html lang="en">
<head>
<meta charset="utf-8">
<title>Bramble Fork Pantry – Recipe Card</title>
<link href="https://fonts.googleapis.com/css2?family=Assistant:wght@300&family=Josefin+Sans:ital,wght@1,600&family=Noto+Serif:ital,wght@1,700&display=swap" rel="stylesheet">
<style>
  :root {
    --ink: #000000;
    --paper: #ffffff;
    --rule: #a09d9e;
  }
  html, body {
    margin: 0;
    padding: 0;
    overflow: hidden;
    background: var(--paper);
  }
  .recipe-card {
    position: relative;
    width: 1200px;
    height: 930px;
    background: var(--paper);
    color: var(--ink);
    overflow: hidden;
  }
  .brand-mark {
    position: absolute;
    left: 121px;
    top: 58px;
    width: 169px;
    height: 213px;
    display: flex;
    flex-direction: column;
    justify-content: center;
    align-items: center;
    font-family: "Assistant", sans-serif;
    font-weight: 300;
    font-size: 34px;
    line-height: 1.05;
    letter-spacing: 2px;
    text-align: center;
    color: var(--ink);
  }
  .masthead {
    position: absolute;
    left: 300px;
    top: 114px;
    width: 612px;
    text-align: center;
  }
  .masthead__web {
    margin: 0;
    font-family: "Josefin Sans", sans-serif;
    font-style: italic;
    font-weight: 600;
    font-size: 19px;
    letter-spacing: 0.3px;
  }
  .masthead__name {
    margin: 4px 0 0;
    font-family: "Assistant", sans-serif;
    font-weight: 300;
    font-size: 54px;
    line-height: 1;
    letter-spacing: 3px;
  }
  .masthead__tagline {
    margin: 3px 0 0;
    font-family: "Noto Serif", serif;
    font-style: italic;
    font-weight: 700;
    font-size: 10px;
  }
  .stamp-box {
    position: absolute;
    left: 935px;
    top: 42px;
    width: 205px;
    height: 227px;
    border: 11px solid var(--ink);
  }
  .divider {
    position: absolute;
    left: 585px;
    top: 303px;
    width: 9px;
    height: 474px;
    background: var(--ink);
  }
  .writing-lines {
    position: absolute;
    left: 640px;
    top: 0;
    width: 475px;
    height: 930px;
    margin: 0;
    padding: 0;
    list-style: none;
  }
  .writing-lines li {
    position: absolute;
    left: 0;
    width: 100%;
    height: 5px;
    background: var(--rule);
  }
</style>
</head>
<body>
  <main class="recipe-card">
    <div class="brand-mark">BRAMBLE<br>FORK<br>PANTRY</div>

    <header class="masthead">
      <p class="masthead__web">www.brambleforkpantry.com</p>
      <h1 class="masthead__name">BRAMBLE FORK PANTRY</h1>
      <p class="masthead__tagline">A friendly kitchen shop for every home cook</p>
    </header>

    <div class="stamp-box" aria-label="Stamp area"></div>

    <div class="divider"></div>

    <ul class="writing-lines" aria-label="Recipe writing lines">
      <li style="top:434px"></li>
      <li style="top:496px"></li>
      <li style="top:557px"></li>
      <li style="top:619px"></li>
      <li style="top:677px"></li>
      <li style="top:740px"></li>
    </ul>
  </main>
</body>
</html>
```